Website for psychology clinic

We need a website for a psychology business by the name of "tranquil harbour psychology". Our psychology practice is based in Melbourne across 3 locations and provides psychological assessment, treatment and support (on an individual and group level) to clients experiencing a range of psychological issues including depression, anxiety, adjustment issues, relationship issues, and specifically eating disorders.
Most of our clients are relatively young with the majority of our clientele being women ranging from adolescence to middle-aged.

Target Market(s)

A range of clients from adolescents to older-aged adults seeking psychological support for issues including depression, anxiety, adjustment issues, and relationship issues. A number of our staff specialise in eating disorders and body image issues (predominantly females) and this makes up a large portion of our business. We would like to market ourselves toward individuals with disordered eating, however would like to encompass a broader range of issues such as those mentioned above.
General Practitioners (doctors) refer largely to our service and therefore would want this to be user friendly

Industry/Entity Type

Clinic

Font styles to use
Sans Serif
Script

Colors
9bcb3c
0455a3
ffffff
85cae6
cee9f5

Requirements
Must have
• Must include logo design (see attached logo) - tranquil harbour

Themes of personal growth, change and development as per my business name and logo - suggestive of a therapeutic journey
Nice to have
• A warm and inviting homepage with a welcoming message -

I really love the website brackenwellcare.co.uk and would love to use this as a guide as to what I would like.
Would like a simple yet elegant - not too wordy website page - something with enough information for the client
I also like the simplicity of clinicpagesnet.com.au and have attached a couple of examples in the images section. brackenwellcare.co.uk is my preference however.
I will add images that I would like to use, ideally I would like the use if quotation bubbles as used in this website
Nice to have the following pages -
HOME page
ABOUT
LOCATION
CONTACT US
GP INFORMATION
PATIENT INFORMATIOn
- include "a client form" page for the client to type their details directly into a form which sends directly to the psychologist
MAKE AN ENQUIRY
LINKS
Should not have
• Should not look too chaotic or crowded

```html
<!DOCTYPE html>
<html lang="en">
<head>
<meta charset="utf-8">
<title>Tranquil Harbour Psychology</title>
<link href="https://fonts.googleapis.com/css2?family=Open+Sans:ital,wght@0,300;0,400;0,600;1,400;1,600&display=swap" rel="stylesheet">
<style>
:root{
  --green:#9bcb3c;
  --blue:#0455a3;
  --blue-dark:#034a8e;
  --sky:#85cae6;
  --sky-pale:#cee9f5;
  --white:#ffffff;
  --text:#333333;
  --muted:#777777;
  --icon:#9a9a9a;
  --rule:#d6d6d6;
  --footer:#2b2b2b;
  --footer-text:#bdbdbd;
}
*{box-sizing:border-box;margin:0;padding:0}
html,body{width:1179px;height:1200px;overflow:hidden;background:var(--white)}
body{font-family:"Open Sans",Arial,sans-serif;color:var(--text);position:relative}
.wrap{position:absolute;left:110px;width:960px}

/* header */
.site-header{top:0;height:140px}
.brand{position:absolute;top:50px;left:0;display:flex;align-items:center;gap:10px}
.brand-mark{width:26px;height:26px;border-radius:50%;background:var(--green)}
.brand-name{font-size:25px;font-weight:600;color:var(--blue);line-height:1.1}
.main-nav{position:absolute;top:80px;right:0;display:flex;height:42px;background:var(--blue)}
.main-nav a{display:flex;align-items:center;padding:0 10px;color:var(--white);text-decoration:none;font-size:13.5px;border-left:1px solid var(--blue-dark);background:linear-gradient(#0a62b4,var(--blue))}
.main-nav a.current{background:linear-gradient(#a8d34c,#8dbf2f);color:#1d3a04;border-left:none}

/* hero */
.hero{top:140px;height:336px;display:flex;gap:7px}
.slider{position:relative;width:712px;height:100%;background:linear-gradient(100deg,#2d9ce0 0%,#5bb9ef 55%,#a6dcf6 100%)}
.slide-photo{position:absolute;left:0;top:0;width:300px;height:100%;background:linear-gradient(180deg,rgba(60,120,170,.25) 0%,rgba(120,110,90,.35) 80%,rgba(150,130,90,.55) 100%)}
.slide-title{position:absolute;right:68px;top:30px;text-align:right;color:var(--white);font-weight:300;font-size:38px;line-height:46px;text-shadow:0 1px 2px rgba(0,0,0,.15)}
.slide-next{position:absolute;right:16px;top:147px;width:32px;height:32px;border-radius:50%;background:rgba(255,255,255,.85);display:flex;align-items:center;justify-content:center}
.testimonial{width:241px;height:100%;background:radial-gradient(circle at 50% 40%,var(--sky-pale) 0%,#a9dbef 60%,var(--sky) 100%);padding:40px 18px 0;text-align:center}
.testimonial blockquote{font-style:italic;font-weight:600;font-size:14.5px;line-height:25px;color:#1f2f3b}
.q{color:var(--blue);font-family:Georgia,serif;font-weight:700;font-size:22px;line-height:0;vertical-align:-4px}
.testimonial cite{display:block;margin-top:18px;font-style:normal;font-size:16px;color:var(--blue)}

/* content */
.content{top:504px;display:flex;gap:10px}
.welcome{width:708px}
h2{font-size:22px;font-weight:600;color:var(--blue);line-height:30px}
.welcome p{font-size:13px;line-height:22px;margin-top:14px}
.welcome .lead{margin-top:20px}
.split{display:flex;gap:19px;margin-top:20px}
.split-photo{width:263px;height:268px;flex:none;background:linear-gradient(180deg,#5da6e0 0%,#a8d2f2 60%,#e8f0f6 80%,#6f9a4a 100%)}
.split-text p{margin-top:0;margin-bottom:8px}
.services{width:242px}
.services h2{text-align:center;margin-left:0}
.service-photo{height:123px;margin-top:9px}
.services h2 + .service-photo{margin-top:17px}
.ph-consult{background:linear-gradient(120deg,#d9c4a8,#7f8b9a 60%,#f0f0f0)}
.ph-thinking{background:linear-gradient(120deg,#c5d4e2,#e8e2dc 60%,#9fb6cc)}
.ph-stones{background:linear-gradient(180deg,#a8cc4a,#7fb03a 60%,#f4f6ef 90%)}

/* contact strip */
.contact{top:1000px;border-top:1px solid var(--rule);padding-top:26px;height:70px;display:flex;justify-content:space-between}
.contact-item{display:flex;align-items:center;gap:12px;font-size:13px;color:var(--muted);line-height:22px}
.contact-item svg{fill:var(--icon)}

/* footer */
.site-footer{position:absolute;left:0;top:1098px;width:1179px;height:102px;background:var(--footer)}
.footer-nav{position:absolute;left:110px;top:22px;font-size:13px;color:var(--footer-text)}
.footer-nav a{color:var(--footer-text);text-decoration:none}
.footer-nav span{margin:0 11px}
.copyright{position:absolute;left:110px;top:58px;font-size:12px;color:var(--footer-text)}
.social{position:absolute;right:114px;top:36px;display:flex;gap:9px}
.social span{width:28px;height:28px;border-radius:50%;background:#8a8a8a}
</style>
</head>
<body>

<header class="wrap site-header">
  <div class="brand">
    <span class="brand-mark"></span>
    <span class="brand-name">tranquil harbour</span>
  </div>
  <nav class="main-nav">
    <a class="current" href="#">Home</a>
    <a href="#">About</a>
    <a href="#">Location</a>
    <a href="#">Contact us</a>
    <a href="#">GP Information</a>
    <a href="#">Patient Information</a>
    <a href="#">Make an Enquiry</a>
    <a href="#">Links</a>
  </nav>
</header>

<section class="wrap hero">
  <div class="slider">
    <div class="slide-photo" role="img" aria-label="Photo of a smiling man sitting on a rock against a blue sky"></div>
    <p class="slide-title">Donec adipiscing felis<br>ultrices vitae.</p>
    <span class="slide-next"><svg width="12" height="14" viewBox="0 0 12 14"><path d="M3 1l6 6-6 6" fill="none" stroke="#8aa4b4" stroke-width="1.6"/></svg></span>
  </div>
  <aside class="testimonial">
    <blockquote><span class="q">&ldquo;</span> Mauris quis velit justo fermentum varius. Morbi porttitor vulputate enim, in semper ligula auctor cursus arcu quis imperdiet faucibus feugiat convallis quam nec ultricies tempor at massa in, tempor congue nisl <span class="q">&rdquo;</span></blockquote>
    <cite>Maya Linden</cite>
  </aside>
</section>

<main class="wrap content">
  <section class="welcome">
    <h2>Welcome to Tranquil Harbour</h2>
    <p class="lead">Pellentesque a felis nunc. Nunc nec facilisis felis. Sed vel porta augue, in dapibus felis. Vestibulum eleifend et lorem a lacinia. Fusce sit amet sem eget augue gravida tincidunt. Sed vitae nunc accumsan, fermentum dolor in, mollis urna. Cras bibendum egestas diam, id ultrices nisi tincidunt ut. Donec iaculis tincidunt placerat. Phasellus eleifend, libero porta sollicitudin fringilla, massa diam aliquam nibh, ullamcorper pulvinar nisl magna sollicitudin turpis. Donec tincidunt orci at diam vestibulum, a pretium justo gravida.</p>
    <div class="split">
      <div class="split-photo" role="img" aria-label="Photo of a happy woman raising her hand under a blue sky above a green field"></div>
      <div class="split-text">
        <p>Curabitur eu ipsum vestibulum, porta nisl ut, scelerisque risus. Etiam elementum ut felis sed vulputate. Praesent pharetra libero in porta malesuada. Suspendisse imperdiet sapien et imperdiet pharetra. Cras dictum nunc eu pharetra laoreet. Curabitur diam risus, ultrices ac turpis et, mattis sodales ante.</p>
        <p>Suspendisse placerat a lectus quis accumsan. Curabitur sed sagittis leo, ac luctus dolor. Suspendisse vitae consectetur dui. Donec pulvinar, eros vitae lobortis tempor, metus purus sagittis metus, id euismod eros diam vel purus. Duis pellentesque libero et ipsum scelerisque tempor. Proin in ante porta, consequat enim id, consectetur turpis. Cras et gravida elit, a eleifend nisi. Phasellus posuere vestibulum eleifend. Nam quis bibendum tortor.</p>
      </div>
    </div>
  </section>
  <aside class="services">
    <h2>Our Services</h2>
    <div class="service-photo ph-consult" role="img" aria-label="Photo of a counselling session with three people talking"></div>
    <div class="service-photo ph-thinking" role="img" aria-label="Photo of a thoughtful man in a shirt"></div>
    <div class="service-photo ph-stones" role="img" aria-label="Photo of stacked black stones with a bamboo shoot on green"></div>
  </aside>
</main>

<section class="wrap contact">
  <div class="contact-item">
    <svg width="24" height="26" viewBox="0 0 24 26"><path d="M1 3h22v23H1zM4 6v17h6V10h4v13h6V6z"/></svg>
    <span>55, Building name, streetname<br>City - Zip code</span>
  </div>
  <div class="contact-item">
    <svg width="28" height="28" viewBox="0 0 28 28"><path d="M4 3l5-2 4 6-3 3c2 4 4 6 8 8l3-3 6 4-2 5c-12 0-21-9-21-21z"/></svg>
    <span>Phone: 612 480 2297</span>
  </div>
  <div class="contact-item">
    <svg width="30" height="28" viewBox="0 0 30 28"><path d="M7 0h14l3 3v6h5v19H1V9h6zM9 2v7h13V4h-3V2zM4 12v14h3V12zm7 2v3h3v-3zm5 0v3h3v-3zm5 0v3h3v-3zm-10 5v3h3v-3zm5 0v3h3v-3zm5 0v3h3v-3z"/></svg>
    <span>Fax : 612 480 2298</span>
  </div>
  <div class="contact-item">
    <svg width="28" height="20" viewBox="0 0 28 20"><path d="M0 0h28v20H0zM2 2l12 9 12-9z" fill-rule="evenodd"/></svg>
    <span>E-mail : info@tranquilharbour.com</span>
  </div>
</section>

<footer class="site-footer">
  <nav class="footer-nav">
    <a href="#">Home</a><span>|</span><a href="#">About</a><span>|</span><a href="#">Location</a><span>|</span><a href="#">Contact us</a><span>|</span><a href="#">GP Information</a><span>|</span><a href="#">Patient Information</a><span>|</span><a href="#">Make an Enquiry</a><span>|</span><a href="#">Links</a>
  </nav>
  <p class="copyright">Copyright &copy; 2013 &nbsp;Tranquil Harbour. &nbsp;All rights reserved.</p>
  <div class="social" aria-label="Social links"><span></span><span></span><span></span></div>
</footer>

</body>
</html>
```